Larchly Business Cards

Create new business cards with the details below.

Trevor Halse
Director

MB: +61 417 352 940
PH: 1300 514 637
Email: trevor.halse@larchly-example.com.au
Address: 27A Pemberly Lane, Ashmere Park VIC 3094 Australia
Website: www.larchly-example.com.au

Requirements
Must have
• must be clean looking

```html
<!DOCTYPE html>
<html lang="en">
<head>
<meta charset="utf-8">
<title>Larchly Business Cards</title>
<link rel="stylesheet" href="https://fonts.googleapis.com/css2?family=Open+Sans:wght@400;600;700&display=swap">
<style>
  :root {
    --lime: #9dc43d;
    --charcoal: #333334;
    --paper: #f3f3f2;
    --ink: #2b2b2b;
    --stage: #2a2a2a;
  }
  * { margin: 0; padding: 0; box-sizing: border-box; }
  html, body { width: 1200px; height: 549px; overflow: hidden; }
  body {
    background: var(--stage);
    font-family: "Open Sans", Arial, sans-serif;
    color: var(--ink);
    position: relative;
  }
  .card {
    position: absolute;
    top: 54px;
    width: 540px;
    height: 338px;
    background: var(--paper);
    overflow: hidden;
  }
  .card--front { left: 53px; }
  .card--back { left: 615px; }

  .brand {
    position: absolute;
    display: flex;
    align-items: center;
    gap: 10px;
    font-weight: 700;
    color: var(--lime);
    letter-spacing: 0.5px;
  }
  .brand__mark { background: var(--lime); display: block; }
  .card--front .brand { left: 19px; top: 96px; font-size: 26px; }
  .card--front .brand__mark { width: 26px; height: 26px; }

  .identity { position: absolute; left: 238px; top: 57px; right: 0; }
  .identity__name, .identity__role {
    height: 30px;
    padding-left: 10px;
    font-size: 19px;
    font-weight: 600;
    color: #fff;
    line-height: 30px;
  }
  .identity__name { background: var(--lime); }
  .identity__role { background: var(--charcoal); }

  .contacts { position: absolute; left: 238px; top: 144px; right: 10px; list-style: none; }
  .contacts__item {
    display: flex;
    align-items: flex-start;
    gap: 11px;
    font-size: 14.5px;
    line-height: 22px;
    margin-bottom: 6px;
    white-space: nowrap;
  }
  .contacts__icon { width: 18px; height: 18px; margin-top: 2px; flex: none; }

  .back__top { position: absolute; left: 0; top: 0; width: 100%; height: 113px; background: var(--lime); }
  .back__bottom {
    position: absolute; left: 0; top: 224px; width: 100%; height: 114px;
    background: var(--charcoal);
    display: flex; align-items: center; justify-content: center;
    color: var(--lime); font-size: 19px; font-weight: 600;
  }
  .card--back .brand {
    left: 0; right: 0; top: 113px; height: 111px;
    justify-content: center; font-size: 44px;
  }
  .card--back .brand__mark { width: 40px; height: 40px; }
</style>
</head>
<body>
  <section class="card card--front" aria-label="Business card front">
    <div class="brand"><span class="brand__mark"></span>Larchly</div>
    <div class="identity">
      <div class="identity__name">Trevor Halse</div>
      <div class="identity__role">Director</div>
    </div>
    <ul class="contacts">
      <li class="contacts__item">
        <svg class="contacts__icon" viewBox="0 0 18 18" aria-hidden="true"><circle cx="9" cy="9" r="9" fill="#9dc43d"/><rect x="6" y="3.5" width="6" height="11" rx="1" fill="none" stroke="#fff" stroke-width="1.3"/></svg>
        +61 417 352 940
      </li>
      <li class="contacts__item">
        <svg class="contacts__icon" viewBox="0 0 18 18" aria-hidden="true"><circle cx="9" cy="9" r="9" fill="#9dc43d"/><path d="M6 4.5 L8 7 L7 8.2 Q8 10.5 9.8 11 L11 10 L13.5 12 L12.3 13.5 Q7.5 13.5 4.5 6 Z" fill="#fff"/></svg>
        1300 514 637
      </li>
      <li class="contacts__item">
        <svg class="contacts__icon" viewBox="0 0 18 18" aria-hidden="true"><rect x="0" y="3" width="18" height="12" fill="#9dc43d"/><path d="M0 3 L9 10 L18 3 M0 15 L7 8.5 M18 15 L11 8.5" fill="none" stroke="#fff" stroke-width="1.2"/></svg>
        trevor.halse@larchly-example.com.au
      </li>
      <li class="contacts__item">
        <svg class="contacts__icon" viewBox="0 0 18 18" aria-hidden="true"><circle cx="9" cy="9" r="9" fill="#9dc43d"/><ellipse cx="9" cy="9" rx="3.5" ry="8" fill="none" stroke="#fff" stroke-width="1"/><path d="M1 9 H17" stroke="#fff" stroke-width="1"/></svg>
        www.larchly-example.com.au
      </li>
      <li class="contacts__item">
        <svg class="contacts__icon" viewBox="0 0 18 18" aria-hidden="true"><path d="M9 18 L3.5 9 A6 6 0 1 1 14.5 9 Z" fill="#9dc43d"/><circle cx="9" cy="6.5" r="2.2" fill="#fff"/></svg>
        <span>27A Pemberly Lane,<br>Ashmere Park, VIC 3094</span>
      </li>
    </ul>
  </section>

  <section class="card card--back" aria-label="Business card back">
    <div class="back__top"></div>
    <div class="brand"><span class="brand__mark"></span>Larchly</div>
    <div class="back__bottom">www.larchly-example.com.au</div>
  </section>
</body>
</html>
```